UPDATE: I have uploaded the selected logo from the other contest, please use it in your designs.

I have a logo design contest as well so not sure how PixelGuild handles that. They should integrate at some point. I will describe the overall theme with the logo description. See it for details.

The business card side of it would just build on that same theme.

Target Market(s)

8-40

Industry/Entity Type

Business

Contact Information for Business Card

FirstName LastName
Email

Logo Text

Velimor

Font styles to use
Sans Serif

Requirements
Must have
• the url Velimor.com somewhere in it.

```html
<!DOCTYPE html>
<html lang="en">
<head>
<meta charset="utf-8">
<title>Velimor Business Card</title>
<link href="https://fonts.googleapis.com/css2?family=Marcellus&family=Marcellus+SC&family=Tinos&display=swap" rel="stylesheet">
<style>
  :root {
    --stage: #2f2f2f;
    --red: #e11f24;
    --black: #050505;
    --white: #ffffff;
    --paper: #f3f3f3;
    --ink-grey: #8a8a8a;
    --accent-line: #f08a5d;
  }
  * { margin: 0; padding: 0; box-sizing: border-box; }
  html, body { width: 1200px; height: 1000px; overflow: hidden; }
  body {
    background: var(--stage);
    position: relative;
    font-family: "Tinos", serif;
  }
  .card {
    position: absolute;
    top: 350px;
    width: 520px;
    height: 300px;
    overflow: hidden;
    box-shadow: 0 14px 30px rgba(0,0,0,.45);
  }
  .card--front { left: 60px; background: var(--red); }
  .card--back { left: 620px; background: var(--paper); }
  .card__shapes { position: absolute; inset: 0; width: 100%; height: 100%; }

  .brand {
    position: absolute;
    font-family: "Marcellus", serif;
    color: var(--white);
    line-height: 1;
    letter-spacing: 2px;
  }
  .card--front .brand { left: 250px; top: 72px; font-size: 58px; }
  .card--back .brand { left: 40px; top: 200px; font-size: 44px; }

  .front-url {
    position: absolute;
    left: 252px;
    top: 150px;
    color: var(--white);
    font-family: "Marcellus", serif;
    font-size: 13px;
    letter-spacing: 7px;
    text-transform: uppercase;
  }

  .holder {
    position: absolute;
    right: 30px;
    top: 18px;
    text-align: right;
    color: var(--white);
    font-family: "Marcellus SC", serif;
  }
  .holder__name { font-size: 17px; letter-spacing: 3px; }
  .holder__role { font-size: 10px; letter-spacing: 2px; margin-top: 2px; }

  .contact {
    position: absolute;
    right: 26px;
    top: 96px;
    width: 220px;
    text-align: right;
    color: var(--ink-grey);
  }
  .contact__row {
    position: relative;
    display: flex;
    justify-content: flex-end;
    align-items: center;
    gap: 8px;
  }
  .contact__address { font-size: 10px; margin-bottom: 12px; }
  .contact__value { font-size: 15px; line-height: 1.15; }
  .contact__group { margin-bottom: 14px; }
  .contact__rule {
    height: 1px;
    width: 130px;
    margin: 3px 22px 0 auto;
    background: linear-gradient(to left, var(--red), var(--accent-line) 60%, transparent);
  }
  .icon { width: 16px; height: 16px; flex: none; }
</style>
</head>
<body>

  <section class="card card--front" aria-label="Business card front">
    <svg class="card__shapes" viewBox="0 0 520 300" aria-hidden="true">
      <polygon points="0,146 168,170 250,300 0,300" fill="var(--white)"/>
      <polygon points="0,154 162,178 240,300 0,300" fill="var(--black)"/>
    </svg>
    <div class="brand">Velimor</div>
    <div class="front-url">www.velimor.com</div>
  </section>

  <section class="card card--back" aria-label="Business card back">
    <svg class="card__shapes" viewBox="0 0 520 300" aria-hidden="true">
      <polygon points="0,0 520,0 520,72 290,128 0,100" fill="var(--black)"/>
      <polygon points="0,107 292,136 375,300 0,300" fill="var(--white)"/>
      <polygon points="0,112 290,140 370,300 0,300" fill="var(--red)"/>
    </svg>

    <div class="holder">
      <div class="holder__name">Your Name</div>
      <div class="holder__role">Owner</div>
    </div>

    <div class="brand">Velimor</div>

    <div class="contact">
      <div class="contact__row contact__address">
        <span>2100, Your street, your city, CA</span>
        <svg class="icon" viewBox="0 0 16 16" aria-hidden="true">
          <path d="M8 1a5 5 0 0 1 5 5c0 4-5 9-5 9S3 10 3 6a5 5 0 0 1 5-5z" fill="var(--red)"/>
          <circle cx="8" cy="6" r="2" fill="var(--white)"/>
        </svg>
      </div>

      <div class="contact__group">
        <div class="contact__row">
          <span class="contact__value">123-456-789<br>123-456-789</span>
          <svg class="icon" viewBox="0 0 16 16" aria-hidden="true">
            <polygon points="4.7,0.5 11.3,0.5 15.5,4.7 15.5,11.3 11.3,15.5 4.7,15.5 0.5,11.3 0.5,4.7" fill="var(--red)"/>
            <rect x="5" y="3.5" width="6" height="9" rx="1" fill="var(--white)"/>
          </svg>
        </div>
        <div class="contact__rule"></div>
      </div>

      <div class="contact__group">
        <div class="contact__row">
          <span class="contact__value">admin@velimor.com<br>www.velimor.com</span>
          <svg class="icon" viewBox="0 0 16 16" aria-hidden="true">
            <polygon points="4.7,0.5 11.3,0.5 15.5,4.7 15.5,11.3 11.3,15.5 4.7,15.5 0.5,11.3 0.5,4.7" fill="var(--red)"/>
            <rect x="4" y="4" width="8" height="6" fill="none" stroke="var(--white)" stroke-width="1.2"/>
            <line x1="3" y1="12" x2="13" y2="12" stroke="var(--white)" stroke-width="1.2"/>
          </svg>
        </div>
        <div class="contact__rule"></div>
      </div>
    </div>
  </section>

</body>
</html>
```